Killer Webpage Design

I currently have a self-hosted webpage through wordpress at www.varnetpixel.com - the content is complete and I'm happy with this but I need it designed (no coding) to complete my requirements. I'm happy to take designs which are non-Wordpress if there is specific advantage in this.

My full branding logos are attached along with color files. My main aim is consistent branding across all areas (social media, business cards, emails, websites). I have the rest running but am not happy with the available default selections from Wordpress.

I would prefer to use the darker blue version of the logo as I feel this has more standout in online media, however I would appreciate submissions with both variants to help me choose.

With the homepage I will also want to see blog pages and category pages designed but this can come after I have selected a design to go with,

Sites that I like and are related to my business include the following:
http://www.plumtally.com/au/accounting-software/
http://www.taskbrindle.com/home.aspx
https://tillnorth.com/register
Updates

Apologies for the confusion - to clarify for designers I am looking for design only, no coding.

FYI - i have now uploaded business cards for an idea of the contemporary style of design completed so far.

Target Market(s)

small to medium business. Not systemised but looking for help and support.

Industry/Entity Type

Business

Requirements
Must have
• I'm looking for a minimalist professional page, with the ability to easily add new sections when required. I will also need a CMS to add blog posts on the go, with the same features that it currently has (comments, social logon etc)

```html
<!DOCTYPE html>
<html lang="en">
<head>
<meta charset="utf-8">
<title>Varnet Pixel — Specialist Business Consultants</title>
<link rel="stylesheet" href="https://fonts.googleapis.com/css2?family=Figtree:wght@400;600;700;800&display=swap">
<style>
  :root {
    --navy: #1a5a78;
    --hero-dark: #1e5f7a;
    --teal: #2ea3b0;
    --teal-text: #2b9aa8;
    --red: #a9283a;
    --orange: #ee7a2a;
    --orange-dark: #d9621a;
    --ink: #1d1d1d;
    --grey: #8a8a8a;
    --text: #3c3c3c;
    --rule: #9a9a9a;
    --white: #ffffff;
  }
  * { margin: 0; padding: 0; box-sizing: border-box; }
  html, body { width: 1200px; height: 1084px; overflow: hidden; background: var(--white); }
  body { font-family: "Figtree", Arial, sans-serif; position: relative; color: var(--text); }
  .abs { position: absolute; }

  /* Header */
  .brand { left: 205px; top: 28px; display: flex; align-items: center; gap: 12px; }
  .brand-dot { width: 60px; height: 60px; border-radius: 50%; background: var(--teal); }
  .brand-name { font-size: 31px; font-weight: 700; color: var(--navy); letter-spacing: -0.5px; }
  .social { left: 584px; top: 53px; display: flex; gap: 4px; }
  .social span { width: 13px; height: 13px; border-radius: 3px; background: #2d2d2d; display: block; }
  .search { left: 818px; top: 47px; width: 174px; height: 23px; border: 1px solid #c9c9c9; border-radius: 2px; display: flex; align-items: center; font-size: 8px; color: #a5a5a5; letter-spacing: .3px; }
  .search svg { margin: 0 6px 0 8px; }
  .search .sep { width: 1px; height: 12px; border-left: 1px dotted #999; margin-right: 6px; }

  .nav { left: 206px; top: 122px; width: 784px; display: flex; justify-content: space-between; align-items: center; font-size: 11px; font-weight: 600; color: var(--navy); letter-spacing: .2px; }
  .nav .div { width: 0; height: 12px; border-left: 1px dotted #888; }

  .rule { left: 200px; width: 796px; height: 0; border-top: 1px dotted var(--rule); }

  /* Hero */
  .hero-band { left: 0; top: 165px; width: 997px; height: 440px; background: var(--hero-dark); }
  .hero-side { left: 997px; top: 165px; width: 203px; height: 440px; background: var(--teal); }
  .hero-photo { left: 546px; top: 168px; width: 450px; height: 437px;
    background: linear-gradient(160deg, #1e5f7a 0%, #233148 45%, #1b2334 70%, #8c2a38 100%); }
  .hero-title { left: 212px; top: 306px; color: var(--white); font-weight: 700; font-size: 47px; letter-spacing: -1px; line-height: 1; }
  .hero-sub { left: 212px; top: 356px; color: var(--white); font-weight: 700; font-size: 26.8px; letter-spacing: .2px; line-height: 1; }
  .hero-copy { left: 213px; top: 392px; width: 330px; color: var(--white); font-size: 10.5px; font-weight: 600; line-height: 13.6px; }
  .cta { left: 211px; top: 452px; width: 226px; height: 45px; border-radius: 5px; background: linear-gradient(180deg, var(--orange) 0%, var(--orange-dark) 100%); color: var(--white); font-weight: 800; font-size: 27px; letter-spacing: -1px; display: flex; align-items: center; justify-content: center; }

  /* Section headings */
  .sec-head { left: 206px; display: flex; align-items: baseline; gap: 4px; }
  .sec-head .big { font-size: 36px; font-weight: 800; color: var(--teal-text); letter-spacing: -1px; }
  .sec-head .small { font-size: 20px; font-weight: 700; color: var(--ink); letter-spacing: -1px; }
  .services-head { top: 618px; }
  .services-line { left: 518px; top: 643px; width: 478px; border-top: 1px dotted #bbb; }
  .services-intro { left: 210px; top: 661px; font-size: 11.1px; color: var(--grey); font-weight: 600; white-space: nowrap; }

  /* Services */
  .col-div { top: 696px; height: 144px; border-left: 1px dotted #bbb; }
  .svc-icon { top: 700px; }
  .svc-title { top: 772px; font-size: 12.5px; font-weight: 700; letter-spacing: .2px; }
  .svc-copy { top: 796px; width: 175px; font-size: 9.5px; line-height: 12.5px; color: var(--text); }
  .plus { top: 826px; width: 17px; height: 17px; border-radius: 50%; }
  .t-red { color: var(--red); } .b-red { background: var(--red); }
  .t-orange { color: var(--orange); } .b-orange { background: var(--orange); }
  .t-teal { color: var(--teal-text); } .b-teal { background: var(--teal); }
  .t-navy { color: var(--navy); } .b-navy { background: var(--navy); }

  /* Welcome */
  .welcome-head { top: 878px; }
  .welcome-copy { left: 206px; top: 918px; width: 752px; font-size: 11px; line-height: 13.6px; color: var(--grey); font-weight: 600; }
  .read-more { left: 206px; top: 970px; font-size: 11px; font-weight: 700; color: var(--navy); }

  /* Footer */
  .foot-links { left: 206px; top: 1031px; font-size: 9px; color: #555; letter-spacing: .1px; white-space: nowrap; }
  .foot-copy { left: 207px; top: 1046px; font-size: 11px; font-weight: 600; color: #555; }
  .foot-copy b { color: var(--navy); font-weight: 600; margin-right: 6px; }
  .foot-mark { left: 952px; top: 1017px; width: 40px; height: 40px; border-radius: 50%; background: var(--teal); }
</style>
</head>
<body>

<header>
  <div class="abs brand"><span class="brand-dot"></span><span class="brand-name">Varnet Pixel</span></div>
  <div class="abs social" aria-label="Social links"><span></span><span></span><span></span><span></span><span></span></div>
  <div class="abs search">
    <svg width="11" height="11" viewBox="0 0 11 11"><circle cx="4.5" cy="4.5" r="3.5" fill="none" stroke="#aaa" stroke-width="1.2"/><line x1="7" y1="7" x2="10" y2="10" stroke="#aaa" stroke-width="1.4"/></svg>
    <span class="sep"></span>ENTER YOUR KEYWORDS
  </div>
  <nav class="abs nav">
    <span>HOME</span><span class="div"></span>
    <span>SOFTWARE TRAINING AND IMPLEMENTATION</span><span class="div"></span>
    <span>PROJECT MANAGMENT</span><span class="div"></span>
    <span>BUSINESS PROCESS ANALYSIS</span><span class="div"></span>
    <span>BLOG</span><span class="div"></span>
    <span>ABOUT US</span>
  </nav>
  <div class="abs rule" style="top:163px"></div>
</header>

<section class="hero">
  <div class="abs hero-band"></div>
  <div class="abs hero-side"></div>
  <div class="abs hero-photo" role="img" aria-label="Portrait photograph of a consultant in a dark suit and red tie"></div>
  <h1 class="abs hero-title">SPECIALIST</h1>
  <h2 class="abs hero-sub">BUSINESS CONSULTANTS</h2>
  <p class="abs hero-copy">Lorem ipsum dolor sit amet, consectetuer adipiscing elit, sed diam nonummy nibh euismod tincidunt ut laoreet dolore magna aliquam erat volutpat.</p>
  <div class="abs cta">JOIN US NOW!</div>
</section>

<section class="services">
  <div class="abs sec-head services-head"><span class="big">SERVICES</span><span class="small">/ WHAT WE DO</span></div>
  <div class="abs services-line"></div>
  <p class="abs services-intro">Lorem ipsum dolor sit amet, consectetuer adipiscing elit, sed diam nonummy nibh euismod tincidunt ut laoreet dolore magna aliquam erat volutpat.</p>

  <div class="abs col-div" style="left:380px"></div>
  <div class="abs col-div" style="left:582px"></div>
  <div class="abs col-div" style="left:819px"></div>

  <svg class="abs svc-icon" style="left:258px" width="60" height="50" viewBox="0 0 60 50">
    <ellipse cx="24" cy="30" rx="17" ry="12" transform="rotate(-35 24 30)" fill="var(--red)"/>
    <line x1="16" y1="36" x2="30" y2="24" stroke="#fff" stroke-width="2"/>
    <path d="M36 20 C44 14 40 4 48 4 C56 4 56 14 50 16" fill="none" stroke="var(--red)" stroke-width="2"/>
  </svg>
  <svg class="abs svc-icon" style="left:460px" width="46" height="50" viewBox="0 0 46 50">
    <circle cx="22" cy="28" r="18" fill="none" stroke="var(--orange)" stroke-width="5"/>
    <path d="M14 26 L21 34 L38 6" fill="none" stroke="var(--orange)" stroke-width="5" stroke-linecap="round"/>
  </svg>
  <svg class="abs svc-icon" style="left:680px" width="50" height="50" viewBox="0 0 50 50">
    <line x1="1" y1="0" x2="1" y2="48" stroke="var(--teal)" stroke-width="1" stroke-dasharray="2 2"/>
    <line x1="0" y1="48" x2="48" y2="48" stroke="var(--teal)" stroke-width="1.5"/>
    <rect x="5" y="34" width="12" height="12" fill="var(--teal)"/>
    <rect x="19" y="22" width="12" height="24" fill="var(--teal)"/>
    <rect x="33" y="8" width="12" height="38" fill="var(--teal)"/>
  </svg>
  <svg class="abs svc-icon" style="left:884px" width="48" height="50" viewBox="0 0 48 50">
    <path d="M6 28 A18 18 0 0 1 42 28" fill="none" stroke="var(--navy)" stroke-width="5"/>
    <rect x="2" y="24" width="9" height="14" rx="3" fill="var(--navy)"/>
    <rect x="37" y="24" width="9" height="14" rx="3" fill="var(--navy)"/>
    <path d="M41 38 Q40 46 28 46" fill="none" stroke="var(--navy)" stroke-width="3"/>
  </svg>

  <h3 class="abs svc-title t-red" style="left:215px">SOFTWARE TRAINING</h3>
  <h3 class="abs svc-title t-orange" style="left:415px">PROJECT MANAGMENT</h3>
  <h3 class="abs svc-title t-teal" style="left:608px">BUSINESS PROCESS ANALYSIS</h3>
  <h3 class="abs svc-title t-navy" style="left:845px">CONSULTING</h3>

  <p class="abs svc-copy" style="left:213px">Lorem ipsum dolor sit amet, consectetuer adipiscing...</p>
  <p class="abs svc-copy" style="left:414px">Lorem ipsum dolor sit amet, consectetuer adipiscing...</p>
  <p class="abs svc-copy" style="left:608px;width:200px">Lorem ipsum dolor sit amet, consectetuer adipiscing...</p>
  <p class="abs svc-copy" style="left:844px">Lorem ipsum dolor sit amet, consectetuer adipiscing...</p>

  <svg class="abs plus b-red" style="left:337px" viewBox="0 0 17 17"><path d="M8.5 4v9M4 8.5h9" stroke="#fff" stroke-width="2"/></svg>
  <svg class="abs plus b-orange" style="left:550px" viewBox="0 0 17 17"><path d="M8.5 4v9M4 8.5h9" stroke="#fff" stroke-width="2"/></svg>
  <svg class="abs plus b-teal" style="left:784px" viewBox="0 0 17 17"><path d="M8.5 4v9M4 8.5h9" stroke="#fff" stroke-width="2"/></svg>
  <svg class="abs plus b-navy" style="left:973px" viewBox="0 0 17 17"><path d="M8.5 4v9M4 8.5h9" stroke="#fff" stroke-width="2"/></svg>

  <div class="abs rule" style="top:862px"></div>
</section>

<section class="welcome">
  <div class="abs sec-head welcome-head"><span class="big">WELCOME</span><span class="small">/ ABOUT US</span></div>
  <p class="abs welcome-copy">Cloud computing spending is due to account for a third of annual IT expenditure growth by the end of 2013. Every year the range of cloud software systems gets bigger, now including Plumtally Accounting, Cloudnest Suite for Business, jobPRISM Job Management Software, Deskwell Workspace, Tallyforge Project Manager and many more.</p>
  <span class="abs read-more">READ MORE</span>
  <div class="abs rule" style="top:1006px"></div>
</section>

<footer>
  <p class="abs foot-links">HOME | SOFTWARE TRAINING AND IMPLEMENTATION | PROJECT MANAGMENT | BUSINESS PROCESS ANALYSIS | BLOG | &nbsp;ABOUT US | CONTACT US</p>
  <p class="abs foot-copy"><b>VARNET PIXEL © 2013</b>Privacy Policy</p>
  <div class="abs foot-mark"></div>
</footer>

</body>
</html>
```